Advertisement for tellmark Ad

We are looking to copy a mailer style design that would normally be sent out to a mailbox. However we have decided to simply use it and run an add on Tellmark. please check photo sizes for tellmark to make sure your design will work.

also please try to use the colors from our website: riverbendhollow@mailnest.com

we want the same layout as the ad we sent in the files, with different photos and color scheme.

Target Market(s)

dog owners with busy schedules

Font styles to use
Sans Serif

Colors

Designer to choose only greyscale colors for use in the design.

```html
<!DOCTYPE html>
<html lang="en">
<head>
<meta charset="utf-8">
<title>Riverbend Hollow Canine Activity Center – Daycare Offer</title>
<link rel="stylesheet" href="https://fonts.googleapis.com/css2?family=Roboto:wght@400;500;700&display=swap">
<style>
  :root {
    --accent-grey: #7b7b7b;
    --ink-white: #ffffff;
    --ink-dark: #1e1e1e;
    --photo-light: #f2f2f2;
    --photo-mid: #d6d6d6;
    --photo-dark: #333333;
    --photo-soft: #8c8c8c;
    --band-top: #575757;
    --band-bottom: #262626;
    --divider: rgba(255, 255, 255, 0.75);
  }

  * { margin: 0; padding: 0; box-sizing: border-box; }

  html, body {
    width: 1200px;
    height: 628px;
    overflow: hidden;
    background: #ffffff;
  }

  .ad {
    position: relative;
    width: 1200px;
    height: 628px;
    font-family: "Roboto", Arial, sans-serif;
    color: var(--ink-white);
    overflow: hidden;
  }

  /* ---------- Hero ---------- */
  .hero {
    position: absolute;
    left: 0; top: 0;
    width: 1200px;
    height: 430px;
  }

  .hero-photo {
    position: absolute;
    left: 0; top: 0;
    width: 640px;
    height: 430px;
    background:
      radial-gradient(ellipse 190px 230px at 120px 230px, var(--photo-dark) 0%, rgba(51,51,51,0.85) 55%, rgba(51,51,51,0) 100%),
      radial-gradient(ellipse 190px 120px at 470px 330px, var(--photo-soft) 0%, rgba(140,140,140,0.8) 50%, rgba(140,140,140,0) 100%),
      linear-gradient(180deg, var(--photo-light) 0%, var(--photo-mid) 100%);
  }

  .hero-panel {
    position: absolute;
    left: 0; top: 0;
    width: 1200px;
    height: 430px;
  }

  .brand {
    position: absolute;
    left: 262px;
    top: 82px;
    display: flex;
    align-items: center;
    gap: 10px;
  }

  .brand-dot {
    width: 22px;
    height: 22px;
    border-radius: 50%;
    background: var(--ink-dark);
  }

  .brand-name {
    font-size: 20px;
    font-weight: 700;
    letter-spacing: 0.5px;
    color: var(--ink-dark);
    text-transform: uppercase;
  }

  .pitch {
    position: absolute;
    left: 690px;
    top: 38px;
    width: 500px;
  }

  .pitch-headline {
    font-size: 40px;
    font-weight: 700;
    line-height: 47px;
    letter-spacing: 1.5px;
    text-transform: uppercase;
  }

  .pitch-points {
    list-style: none;
    margin-top: 26px;
  }

  .pitch-points li {
    font-size: 24.5px;
    font-weight: 500;
    letter-spacing: 1.1px;
    line-height: 28px;
    text-transform: uppercase;
    margin-bottom: 12px;
  }

  .pitch-points .footnote {
    display: block;
    font-size: 14px;
    font-weight: 400;
    line-height: 16px;
    letter-spacing: 0.6px;
  }

  .contact {
    position: absolute;
    left: 690px;
    top: 318px;
    font-size: 20px;
    font-weight: 500;
    line-height: 27px;
    letter-spacing: 0.3px;
    font-style: normal;
  }

  .contact .phone { font-weight: 700; }

  /* ---------- Offer band ---------- */
  .offers {
    position: absolute;
    left: 0; top: 430px;
    width: 1200px;
    height: 198px;
    display: flex;
    background: linear-gradient(180deg, var(--band-top) 0%, var(--band-bottom) 100%);
  }

  .offer {
    text-align: center;
    padding-top: 26px;
  }

  .offer-daycare { width: 408px; }
  .offer-bath { width: 402px; border-left: 1px dashed var(--divider); }
  .offer-groom { width: 390px; border-left: 1px dashed var(--divider); }

  .offer-title {
    font-size: 35px;
    font-weight: 700;
    line-height: 42px;
    letter-spacing: 1.2px;
    text-transform: uppercase;
  }

  .offer-terms {
    margin-top: 6px;
    font-size: 15px;
    font-weight: 400;
    line-height: 19px;
  }
</style>
</head>
<body>
<main class="ad">
  <section class="hero">
    <div class="hero-photo" role="img" aria-label="Studio photo of two dogs lying together on a white backdrop"></div>

    <svg class="hero-panel" width="1200" height="430" viewBox="0 0 1200 430" aria-hidden="true">
      <polygon points="568,0 1200,0 1200,430 625,430" fill="var(--accent-grey)"/>
    </svg>

    <div class="brand">
      <span class="brand-dot"></span>
      <span class="brand-name">Riverbend Hollow</span>
    </div>

    <div class="pitch">
      <h1 class="pitch-headline">Not your typical<br>dog daycare</h1>
      <ul class="pitch-points">
        <li>Safe. Open-play daycare</li>
        <li>Exercise &amp; education</li>
        <li>Fun-filled days with their BFFF
          <span class="footnote">(BEST FURRY FRIEND FOREVER)</span>
        </li>
      </ul>
    </div>

    <address class="contact">
      Riverbend Hollow, Canine Activity Center 2418<br>
      North Birch Avenue Maple Falls IA<br>
      <span class="phone">555-014-2290</span>
    </address>
  </section>

  <section class="offers">
    <article class="offer offer-daycare">
      <h2 class="offer-title">Free first day<br>of daycare!*</h2>
      <p class="offer-terms">*Advanced reservation required.<br>Call to schedule your appointment.<br>Use by 8/31/20</p>
    </article>
    <article class="offer offer-bath">
      <h2 class="offer-title">One free<br>bath!*</h2>
      <p class="offer-terms">*Advanced reservation required.<br>Call to schedule your appointment.<br>Use by 8/31/20</p>
    </article>
    <article class="offer offer-groom">
      <h2 class="offer-title">$20 off first<br>groom!*</h2>
      <p class="offer-terms">*Advanced reservation required.<br>Call to schedule your appointment.<br>Use by 8/31/20</p>
    </article>
  </section>
</main>
</body>
</html>
```